KALMO-VIT Banner

I need a banner for a outpatient (poli clinic) psychiatric clinic/ mental health care center.
The name of the out-patient clinic is ' KALMO-VIT ' . It is written in capitals. The colour we use is green. Just look at the uploaded files and on our website: WWW.KALMO-VIT.NL

KALMO-VIT is mainly based in the city Groningen, the Netherlands (Holland).

If it is possible, I would also like to have a QR-code of our website on the banner. It should be a vertical banner.

We want to print big vertical flags/ roll-up banners

Reason: I just extended the deadline. I will attach more examples of what I want.

To all designers,

Sorry for not giving feedback on your designs. I have attached a picture that I want to be used as background.

So the colour of the banner should be greenish, with the text: "  KALMO-VIT " 
Further more I would like to have the website on the banner: " WWW.KALMO-VIT.NL "
The logo of KALMO-VIT must also be on the banner
And also a small QR-code

I will extend the deadline till february 13th

thanks,

Joost

Reason: Dear designers, Sorry for not reacting. I was ill and could not work. best regards, Joost

Mental Health

• The logo of KALMO-VIT must be in the design. For the right colour just take a look at the attached files and our website: www.KALMO-VIT.NL

```html
<!DOCTYPE html>
<html lang="en">
<head>
<meta charset="utf-8">
<title>KALMO-VIT Banner</title>
<link rel="stylesheet" href="https://fonts.googleapis.com/css2?family=Tinos&family=Libre+Baskerville&family=Carlito&display=swap">
<style>
  :root {
    --green: #0f8a1e;
    --green-deep: #0a7a16;
    --green-line: #3aa845;
    --ink: #1a1a1a;
    --white: #ffffff;
    --grass-1: #cfe6a8;
    --grass-2: #7fb94a;
    --grass-3: #eef4e4;
    --scrub-1: #c9dcee;
    --scrub-2: #eef3f8;
    --gear-1: #f5a623;
    --gear-2: #e2452b;
    --gear-3: #39a9d9;
  }
  * { margin: 0; padding: 0; box-sizing: border-box; }
  html, body { width: 711px; height: 1200px; overflow: hidden; background: var(--white); }
  .canvas { position: relative; width: 711px; height: 1200px; background: var(--white); }
  .banner {
    position: absolute; left: 107px; top: 0; width: 496px; height: 1200px;
    border-left: 1px solid var(--green-line); border-right: 1px solid var(--green-line);
    background: var(--white); overflow: hidden;
  }
  .band-top { position: absolute; left: 0; top: 0; width: 100%; height: 29px; background: var(--green); }
  .band-bottom { position: absolute; left: 0; bottom: 0; width: 100%; height: 60px; background: var(--green); }

  .hero {
    position: absolute; left: 0; top: 29px; width: 100%; height: 300px;
    background:
      radial-gradient(ellipse at 35% 15%, rgba(255,255,255,0.95) 0%, rgba(255,255,255,0) 45%),
      linear-gradient(180deg, var(--grass-1) 0%, var(--grass-2) 45%, var(--grass-3) 80%, var(--white) 100%);
  }
  .brand {
    position: absolute; left: 67px; top: 46px;
    font-family: "Tinos", serif; font-size: 46px; color: var(--green);
    letter-spacing: 1px; display: flex; align-items: center; gap: 12px;
  }
  .brand-dot { width: 26px; height: 26px; border-radius: 50%; background: var(--green); }
  .tagline {
    position: absolute; font-family: "Tinos", serif; color: var(--white);
    -webkit-text-stroke: 1px var(--green-deep); white-space: nowrap;
  }
  .tagline-1 { left: 13px; top: 137px; font-size: 31px; }
  .tagline-2 { left: 13px; top: 198px; font-size: 31px; }
  .tagline-3 { right: 8px; top: 262px; font-size: 30px; }

  .care-photo {
    position: absolute; left: 13px; top: 380px; width: 480px; height: 213px;
    background:
      radial-gradient(ellipse at 30% 50%, var(--scrub-1) 0%, rgba(201,220,238,0) 60%),
      radial-gradient(ellipse at 75% 55%, #d6dde6 0%, rgba(214,221,230,0) 55%),
      var(--scrub-2);
    -webkit-mask-image: linear-gradient(180deg, #000 75%, transparent 100%);
            mask-image: linear-gradient(180deg, #000 75%, transparent 100%);
  }

  .welcome {
    position: absolute; left: 27px; top: 645px;
    font-family: "Libre Baskerville", serif; font-size: 33px; color: var(--green);
  }
  .services {
    position: absolute; left: 27px; top: 703px; list-style: none;
    font-family: "Libre Baskerville", serif; font-size: 25px; color: var(--ink);
    line-height: 53px;
  }
  .gear-art {
    position: absolute; left: 320px; top: 693px; width: 173px; height: 127px;
    border-radius: 50% 45% 45% 50%;
    background: radial-gradient(circle at 45% 45%, var(--gear-2) 0%, var(--gear-1) 45%, var(--gear-3) 80%, rgba(57,169,217,0) 100%);
  }

  .contact {
    position: absolute; left: 0; top: 915px; width: 100%; text-align: center;
    font-family: "Carlito", sans-serif; color: var(--green);
  }
  .contact-phone { font-size: 36px; line-height: 44px; }
  .contact-center { font-size: 25px; margin-top: 14px; letter-spacing: 0.3px; }
  .contact-web { margin-top: 12px; font-size: 20px; line-height: 27px; color: var(--ink); }
</style>
</head>
<body>
<div class="canvas">
  <div class="banner">
    <div class="band-top"></div>

    <div class="hero" role="img" aria-label="Sunlit meadow of dewy green grass"></div>
    <div class="brand"><span>KALMO-VIT</span><span class="brand-dot"></span></div>
    <p class="tagline tagline-1">IT TAKES</p>
    <p class="tagline tagline-2">COURAGE to ASK For HELP</p>
    <p class="tagline tagline-3">With a mental illness.</p>

    <div class="care-photo" role="img" aria-label="Smiling doctor in blue scrubs with a stethoscope, colleagues caring for a patient in the background"></div>

    <h1 class="welcome">Welcome to KALMO-VIT</h1>
    <ul class="services">
      <li>Center for</li>
      <li>Psychological &amp;</li>
      <li>Neuro Psychiatric Services!</li>
    </ul>
    <div class="gear-art" role="img" aria-label="Colourful brain made of interlocking gears"></div>

    <div class="contact">
      <p class="contact-phone">NEED HELP? 555-010-020</p>
      <p class="contact-center">MENTAL HEALTH CARE CENTER</p>
      <p class="contact-web">Email- info@kalmo-vit.nl<br>www.kalmo-vit.nl</p>
    </div>

    <div class="band-bottom"></div>
  </div>
</div>
</body>
</html>
```